Personal Finance Blog Wordpress Design

We are looking for a new Wordpress theme design for CoinHarbor.com.

All of the elements that are currently on the homepage should remain, minus the archives list. The placement of various elements can be changed, we just need a more modern and clean feel. We would like to add a 160 x 600 ad unit on the homepage. We would like the 728x90 ad to be below the navigation similar to that of: http://www.plumtreeledger.example/blog/

We like the fonts used on: http://www.quillpocket.example/blog/

The text that currently resides at the bottom of CoinHarbor.com needs to remain on the homepage, but wherever it is placed needs to not be intrusive.

The color scheme needs to appropriately compliment the logo.

No sliders. I don't like sliders.

I am happy to answer questions.

Industry/Entity Type

Finance

Requirements
Must have
• Included in project description
Nice to have
Should not have
• Included in project description. Don't use sliders

```html
<!DOCTYPE html>
<html lang="en">
<head>
<meta charset="utf-8">
<title>CoinHarbor — Personal Finance Blog</title>
<link rel="stylesheet" href="https://fonts.googleapis.com/css2?family=Alegreya:wght@400&family=Lustria&family=Nunito:wght@400&display=swap">
<style>
  :root{
    --green-dark:#1f5a1f;
    --green-title:#1d5c17;
    --green-btn:#24bf2a;
    --nav-text:#1c351c;
    --rss:#efad4e;
    --border:#dcdcdc;
    --rule:#e6e6e6;
    --panel-head:#f5f5f5;
    --text:#222;
    --muted:#555;
    --accent-line:#dbeeb4;
    --icon:#3b3b3b;
  }
  *{box-sizing:border-box;margin:0;padding:0}
  html,body{width:1200px;height:1000px;overflow:hidden;background:#fff}
  body{position:relative;font-family:"Lustria",Georgia,serif;color:var(--text)}
  .abs{position:absolute}

  .site-header{left:0;top:0;width:1200px;height:54px;border-bottom:2px solid var(--accent-line)}
  .brand{left:16px;top:10px;display:flex;align-items:center;gap:8px}
  .brand-mark{width:30px;height:30px;background:#c9c9c9;border-radius:3px}
  .brand-name{font-family:"Lustria",Georgia,serif;font-size:23px;color:var(--green-dark)}
  .main-nav a{position:absolute;top:18px;font-family:Arial,Helvetica,sans-serif;font-size:13px;color:var(--nav-text);text-decoration:none;white-space:nowrap}

  .ad-banner{left:279px;top:71px;width:642px;height:82px;border:1px solid var(--border);border-radius:4px}
  .ad-label{position:absolute;top:12px;font-family:"Nunito",Arial,sans-serif;font-size:44px;color:#2b2b2b;text-decoration:line-through;text-decoration-thickness:2px;white-space:nowrap}

  .rule{height:1px;background:var(--rule)}

  .featured{left:80px;top:189px;width:780px;height:493px;border:1px solid var(--border);border-radius:3px}
  .photo{display:block}
  .post-title{font-family:"Alegreya",Georgia,serif;font-size:22px;line-height:23px;color:var(--green-title);font-weight:400;white-space:nowrap}
  .post-excerpt{font-size:12.5px;line-height:18px;text-align:justify;color:var(--text)}
  .btn-more{display:flex;align-items:center;justify-content:center;background:var(--green-btn);color:#fff;font-size:13px;border-radius:3px;height:30px;width:92px}

  .category-card{top:737px;height:280px;border:1px solid var(--border);border-radius:3px}
  .tag{position:absolute;top:4px;height:26px;padding:0 10px;display:flex;align-items:center;font-size:11px;color:#fff;border-radius:2px}
  .tag-cat{left:4px;background:var(--green-btn)}
  .tag-rss{right:4px;background:var(--rss)}
  .card-photo{position:absolute;left:4px;right:4px;top:48px;bottom:0}

  .widget{left:874px;width:233px;border:1px solid var(--border);border-radius:3px;background:#fff}
  .social-icon{position:absolute;top:16px;width:33px;height:33px;background:var(--icon);border-radius:6px}
  .widget-title{font-family:"Alegreya",Georgia,serif;font-size:22px;color:#222;font-weight:400}
  .widget-head{height:43px;background:var(--panel-head);border-bottom:1px solid var(--border);padding:8px 13px}
  .widget-text{font-size:12px;line-height:23px;color:var(--text)}
  .widget-text span{display:block;white-space:nowrap;text-align:justify;text-align-last:justify}
  .widget-text span.last{text-align-last:left}
  .input-group{position:absolute;left:13px;width:206px;height:30px;border:1px solid #ccc;border-radius:3px;display:flex;font-size:12.5px;color:#555}
  .input-addon{width:35px;border-right:1px solid #ccc;background:#eee;display:flex;align-items:center;justify-content:center}
  .input-field{flex:1;display:flex;align-items:center;padding-left:11px}
  .input-btn{width:35px;border-left:1px solid #ccc;display:flex;align-items:center;justify-content:center}
  .recent-list li{list-style:none;border-top:1px solid var(--border);padding:9.5px 13px;font-size:12px;line-height:23px;color:var(--muted);white-space:nowrap;overflow:hidden}
</style>
</head>
<body>

<header class="site-header abs">
  <div class="brand abs">
    <span class="brand-mark"></span>
    <span class="brand-name">CoinHarbor</span>
  </div>
  <nav class="main-nav">
    <a style="left:396px">Auto</a>
    <a style="left:448px">Bank Accounts</a>
    <a style="left:558px">Credit Cards</a>
    <a style="left:656px">Insurance</a>
    <a style="left:738px">Investments</a>
    <a style="left:831px">Mortgages</a>
    <a style="left:918px">Personal Finance</a>
    <a style="left:1043px">Small Business</a>
    <a style="left:1155px">Taxes</a>
  </nav>
</header>

<div class="ad-banner abs">
  <span class="ad-label" style="left:7px">Sample Adds</span>
  <span class="ad-label" style="left:360px">Sample Adds</span>
</div>
<div class="rule abs" style="left:93px;top:171px;width:1014px"></div>

<section class="featured abs">
  <div class="photo abs" role="img" aria-label="Tall stack of colourful paper folders and files" style="left:40px;top:24px;width:198px;height:210px;background:linear-gradient(180deg,#f3f3f3 0%,#d8b8a4 35%,#c95e5a 60%,#5fb08a 85%,#e9e9e9 100%)"></div>
  <h2 class="post-title abs" style="left:39px;top:243px">How Long Should<br>You Keep Your Tax<br>Records?</h2>
  <p class="post-excerpt abs" style="left:39px;top:314px;width:199px">When it comes to filing tax returns, many people are always nervous about the possibility of finding out they are being audited by the Internal</p>
  <a class="btn-more abs" style="left:146px;top:411px">Read More »</a>

  <div class="abs" style="left:250px;top:14px;width:1px;height:447px;background:var(--rule)"></div>

  <div class="photo abs" role="img" aria-label="Motorhome driving on a road toward snowy mountains" style="left:294px;top:18px;width:130px;height:128px;background:linear-gradient(180deg,#9ec3e6 0%,#d6e0ea 35%,#6f8f5a 60%,#7b7f84 100%)"></div>
  <h2 class="post-title abs" style="left:446px;top:25px">Road Trip Anyone? Check<br>Out These Great Spring RV<br>Financing Deals</h2>
  <p class="post-excerpt abs" style="left:446px;top:97px;width:295px">Summertime means taking vacations and having fun in the sun. And</p>
  <a class="btn-more abs" style="left:649px;top:141px">Read More »</a>

  <div class="rule abs" style="left:278px;top:209px;width:474px"></div>

  <div class="photo abs" role="img" aria-label="Close-up of a dictionary page defining bankruptcy" style="left:294px;top:231px;width:130px;height:129px;background:linear-gradient(135deg,#5a6472 0%,#c8ccd2 50%,#4a5360 100%)"></div>
  <h2 class="post-title abs" style="left:446px;top:239px">What’s the Difference<br>Between Chapter 7 and<br>Chapter 13 Bankruptcy?</h2>
  <p class="post-excerpt abs" style="left:446px;top:310px;width:295px">Bankruptcy is a powerful financial tool for people who have gotten themselves in over their heads with debt. Consumers might file bankruptcy after the...</p>
  <a class="btn-more abs" style="left:649px;top:390px">Read More »</a>
</section>

<div class="rule abs" style="left:80px;top:718px;width:780px"></div>

<article class="category-card abs" style="left:93px;width:234px">
  <span class="tag tag-cat">Auto</span><span class="tag tag-rss">RSS</span>
  <div class="card-photo" role="img" aria-label="Motorhome on a mountain road" style="background:linear-gradient(180deg,#9ec3e6 0%,#dfe6ee 30%,#6f8f5a 55%,#80858a 100%)"></div>
</article>
<article class="category-card abs" style="left:353px;width:233px">
  <span class="tag tag-cat">Bank Accounts</span><span class="tag tag-rss">RSS</span>
  <div class="card-photo" role="img" aria-label="Blue emblem of a globe held in open hands" style="background:linear-gradient(180deg,#ffffff 0%,#1b1fa0 30%,#2a2db0 70%,#ffffff 100%)"></div>
</article>
<article class="category-card abs" style="left:612px;width:235px">
  <span class="tag tag-cat">Credit Cards</span><span class="tag tag-rss">RSS</span>
  <div class="card-photo" role="img" aria-label="Person holding out a credit card toward the camera" style="background:linear-gradient(160deg,#6d3b3b 0%,#b0243a 30%,#b58a75 55%,#8a4a35 100%)"></div>
</article>

<aside>
  <div class="widget abs" style="top:189px;height:241px">
    <span class="social-icon" role="img" aria-label="Social profile" style="left:26px"></span>
    <span class="social-icon" role="img" aria-label="Social profile" style="left:77px"></span>
    <span class="social-icon" role="img" aria-label="RSS feed" style="left:128px"></span>
    <span class="social-icon" role="img" aria-label="Social profile" style="left:179px"></span>
    <div class="rule abs" style="left:13px;top:71px;width:206px"></div>
    <h3 class="widget-title abs" style="left:13px;top:86px">E-mail Newsletter</h3>
    <p class="widget-text abs" style="left:13px;top:113px;width:206px">
      <span>Sign up now to receive breaking</span>
      <span>news and to hear what's new with</span>
      <span class="last">our website!</span>
    </p>
    <div class="input-group" style="top:191px">
      <span class="input-addon"><svg width="13" height="10" viewBox="0 0 13 10"><path d="M0 0h13v10H0z" fill="#444"/><path d="M0 0l6.5 5L13 0" fill="none" stroke="#eee" stroke-width="1.2"/></svg></span>
      <span class="input-field">Your email</span>
      <span class="input-btn"><svg width="12" height="10" viewBox="0 0 12 10"><path d="M1 5l3.5 3.5L11 1.5" fill="none" stroke="#222" stroke-width="2"/></svg></span>
    </div>
  </div>

  <div class="widget abs" style="top:443px;height:100px">
    <div class="widget-head"><h3 class="widget-title">Search this Site</h3></div>
    <div class="input-group" style="top:55px">
      <span class="input-field">Search</span>
      <span class="input-btn"><svg width="12" height="12" viewBox="0 0 12 12"><circle cx="5" cy="5" r="3.8" fill="none" stroke="#222" stroke-width="1.6"/><path d="M7.8 7.8L11 11" stroke="#222" stroke-width="1.8"/></svg></span>
    </div>
  </div>

  <div class="widget abs" style="top:561px;height:414px">
    <div class="widget-head" style="border-bottom:0"><h3 class="widget-title">Recent Posts</h3></div>
    <ul class="recent-list">
      <li>How Long Should You Keep Your<br>Tax Records?</li>
      <li>Road Trip Anyone? Check Out<br>These Great Spring RV Financing<br>Deals</li>
      <li>What’s the Difference Between<br>Chapter 7 and Chapter 13<br>Bankruptcy?</li>
      <li>Redwood Ridge Fund: A Historical<br>Rundown</li>
      <li>Inexpensive Ways to Add Sources of<br>Fiber to Your Diet</li>
    </ul>
  </div>

  <div class="widget abs" style="top:993px;height:40px"></div>
</aside>

</body>
</html>
```